Ozark Hollowpine Barbeque Sauce*

Design a branded label for a bottle of sauce..... for OZARK HOLLOWPINE BBQ
FOOD LABEL. Target audience is woman buying bbq sauce for men. There is a lot of competition in the market so Texas should really be a highlight. LOGO SHOULD BE BIG. PLEASE RECREATE IF YOU CAN.

I am looking for a unique die cut....

Target Market(s)

GENERAL GROCERY STORE

Industry/Entity Type

Retail

Colors
f58946
ec1f27
f78f20
fee18a
f48541

Requirements
Must have
• OZARK HOLLOWPINE BBQ SAUCE
Nice to have
• ILLUSTRATIONS
Should not have
• NO PICTURES BUT

```html
<!DOCTYPE html>
<html lang="en">
<head>
<meta charset="utf-8">
<title>Ozark Hollowpine BBQ Sauce – Labels</title>
<link rel="stylesheet" href="https://fonts.googleapis.com/css2?family=Playfair+Display:wght@900&family=Archivo:wght@400;700;900&display=swap">
<style>
  :root{
    --backdrop:#efefef;
    --label-red:#ec1f27;
    --paper:#f4f2ee;
    --ink:#111111;
    --amber:#f78f20;
    --orange:#f58946;
    --butter:#fee18a;
    --coral:#f48541;
  }
  *{margin:0;padding:0;box-sizing:border-box}
  html,body{width:1200px;height:1200px;overflow:hidden}
  body{background:var(--backdrop);position:relative;font-family:"Archivo",Arial,sans-serif;color:var(--ink)}

  .front-label{position:absolute;left:70px;top:250px;width:600px;height:700px}
  .front-label .arc-name{font-family:"Archivo",Arial,sans-serif;font-weight:900;font-size:22px;letter-spacing:1.5px;fill:var(--ink)}
  .front-label .hero-word{font-family:"Playfair Display",Georgia,serif;font-weight:900;font-size:92px;fill:var(--ink)}
  .front-label .sub-word{font-family:"Archivo",Arial,sans-serif;font-weight:700;font-size:34px;letter-spacing:1px;fill:var(--label-red)}
  .front-label .volume{font-family:"Archivo",Arial,sans-serif;font-weight:700;font-size:20px;fill:var(--ink)}

  .back-label{position:absolute;left:790px;top:250px;width:330px;height:700px;background:var(--label-red);border-radius:26px 26px 6px 6px;padding:14px}
  .back-inner{width:100%;height:100%;background:var(--paper);border-radius:16px 16px 2px 2px;display:flex;flex-direction:column;align-items:center;padding:10px 14px 0}
  .back-brand{width:100%;height:120px;overflow:visible}
  .back-brand .arc-name{font-family:"Archivo",Arial,sans-serif;font-weight:900;font-size:14px;letter-spacing:1px;fill:var(--ink)}

  .nutrition{width:100%;border:1.5px solid var(--ink);padding:4px 6px;font-size:10.5px;line-height:1.35;margin-top:6px}
  .nutrition h2{font-family:"Archivo",Arial,sans-serif;font-weight:900;font-size:22px;line-height:1.05}
  .nutrition .thick{border-bottom:7px solid var(--ink);padding-bottom:2px}
  .nutrition .mid{border-bottom:4px solid var(--ink)}
  .nutrition .row{display:flex;justify-content:space-between;border-top:1px solid var(--ink)}
  .nutrition .row.first{border-top:none}
  .nutrition .indent{padding-left:12px}
  .nutrition b{font-weight:900}
  .nutrition .tiny{font-size:8.5px;font-weight:900}
  .nutrition .right{text-align:right;font-size:9px;font-weight:900;border-top:3px solid var(--ink)}
  .nutrition .foot{font-size:8px;font-weight:700;border-top:1px solid var(--ink);padding-top:2px}
  .back-copy{width:100%;font-size:10px;line-height:1.45;margin-top:8px}
  .back-art{width:100%;height:92px;margin-top:auto;border-radius:40px 40px 0 0;background:linear-gradient(90deg,var(--butter),var(--amber) 40%,var(--label-red))}
</style>
</head>
<body>

<svg class="front-label" viewBox="0 0 600 700" aria-label="Front label">
  <defs>
    <path id="front-arc" d="M150,300 A160,160 0 0 1 450,300"/>
    <linearGradient id="grill-tones" x1="0" x2="1">
      <stop offset="0" stop-color="#fee18a"/>
      <stop offset="0.45" stop-color="#f78f20"/>
      <stop offset="1" stop-color="#ec1f27"/>
    </linearGradient>
  </defs>
  <g fill="var(--label-red)" stroke="var(--label-red)" stroke-width="30" stroke-linejoin="miter">
    <polygon points="300,100 397,267 585,307 457,451 476,643 300,565 124,643 143,451 15,307 203,267"/>
    <circle cx="300" cy="330" r="200"/>
  </g>
  <g fill="var(--paper)">
    <polygon points="300,100 397,267 585,307 457,451 476,643 300,565 124,643 143,451 15,307 203,267"/>
    <circle cx="300" cy="330" r="200"/>
  </g>
  <text class="arc-name"><textPath href="#front-arc" startOffset="50%" text-anchor="middle">OZARK HOLLOWPINE BBQ</textPath></text>
  <circle cx="300" cy="310" r="56" fill="var(--amber)"/>
  <text class="hero-word" x="300" y="460" text-anchor="middle">OZARK</text>
  <text class="sub-word" x="300" y="505" text-anchor="middle">HOLLOWPINE</text>
  <text class="sub-word" x="300" y="545" text-anchor="middle">BBQ SAUCE</text>
  <text class="volume" x="160" y="570">150 ml</text>
  <rect x="232" y="558" width="200" height="64" rx="28" fill="url(#grill-tones)" role="img" aria-label="Illustration of a kettle grill with flames, tongs and a grilled steak"/>
</svg>

<div class="back-label">
  <div class="back-inner">
    <svg class="back-brand" viewBox="0 0 300 120" aria-label="OZARK HOLLOWPINE BBQ">
      <defs><path id="back-arc" d="M35,85 A115,72 0 0 1 265,85"/></defs>
      <text class="arc-name"><textPath href="#back-arc" startOffset="50%" text-anchor="middle">OZARK HOLLOWPINE BBQ</textPath></text>
      <circle cx="150" cy="78" r="32" fill="var(--amber)"/>
    </svg>

    <div class="nutrition">
      <div class="thick">
        <h2>Nutrition Facts</h2>
        <div>Serving Size: 2 Tbsp (30g)</div>
        <div>Servings Per Container: About 17</div>
      </div>
      <div class="tiny">Amount Per Serving</div>
      <div class="row"><span><b>Calories</b> 10</span><span>Calories from Fat 0</span></div>
      <div class="right">% Daily Value*</div>
      <div class="row"><span><b>Total Fat</b> 0g</span><b>0%</b></div>
      <div class="row indent"><span>Saturated Fat 0g</span><b>0%</b></div>
      <div class="row indent"><span><i>Trans</i> Fat 0g</span><span></span></div>
      <div class="row"><span><b>Cholesterol</b> 0mg</span><b>0%</b></div>
      <div class="row"><span><b>Sodium</b> 200mg</span><b>8%</b></div>
      <div class="row"><span><b>Total Carbohydrate</b> 2g</span><b>1%</b></div>
      <div class="row indent"><span>Dietary Fiber 0g</span><b>0%</b></div>
      <div class="row indent"><span>Sugars 0g</span><span></span></div>
      <div class="row mid"><span><b>Protein</b> 0g</span><span></span></div>
      <div class="row first"><span>Vitamin A &nbsp; 2% &nbsp;•</span><span>Vitamin C &nbsp; 2%</span></div>
      <div class="row"><span>Calcium &nbsp; 0% &nbsp;•</span><span>Iron &nbsp; 0%</span></div>
      <div class="foot">*Percent Daily Values are based on a 2,000 calorie diet.</div>
    </div>

    <p class="back-copy">Slow-simmered in small batches with sun-ripened tomatoes, dark molasses, cracked black pepper and a whisper of hickory smoke. Brush on ribs, brisket or chicken during the last minutes of grilling, or serve warm at the table for dipping. Refrigerate after opening.</p>

    <div class="back-art" role="img" aria-label="Illustration of a kettle grill with flames, tongs and a grilled steak"></div>
  </div>
</div>

</body>
</html>
```